Hollerby Consulting needs a quality & professional business card!

I am a recruitment and employment consultant from Brisbane, Australia and I had a fantastic logo organised by this community to I am hoping the business card will be the same.

I have attached the Hollerby consulting logo that ideally would feature on the back of the business card. There are a number of logos for you to use as you see fit. I would like the colour cheme to match that of the Hollerby Consulting logo. I also have a secondary company called Career Lantern Australia and I have included that logo as well. While it is an important part of the business I don't want this logo feature too predominantly as I am moving out of this space. This logo was created by myself and is of low quality. Feel free to use the icon and words however you want. The winning design will be smart, professional and eye-catching.

The information I am looking for in the business card is:
Name: Derek Hollerby
Position: Founder & Director
Phone: (07) 3156 4082
Mobile: 0418 672 051
Email: derek@careerlantern-example.com.au

Target Market(s)

Recruiters, government, large companies

Contact Information for Business Card

Name: Derek Hollerby
Phone: (07) 3156 4082
Mobile: 0418 672 051
Web: www.careerlantern-example.com.au

Font styles to use
Serif
Sans Serif

Requirements
Must have
• Hollerby Consulting Logo on reverse side
• Contact details on front side with smaller reference to Hollerby Consulting logo and Career Lantern Australia logo

```html
<!DOCTYPE html>
<html lang="en">
<head>
<meta charset="utf-8">
<title>Hollerby Consulting – Business Card</title>
<link rel="stylesheet" href="https://fonts.googleapis.com/css2?family=Roboto:wght@400;500&family=Montserrat:wght@300;500&family=Tinos:wght@700&display=swap">
<style>
  :root {
    --page: #e9e6e1;
    --card-white: #fbfbfb;
    --ink-dark: #232527;
    --ink-mid: #3a3d40;
    --accent-blue: #2a92cc;
    --back-blue: #1689c4;
    --text-light: #ffffff;
    --text-grey: #555a5e;
  }
  * { margin: 0; padding: 0; box-sizing: border-box; }
  html, body {
    width: 1200px; height: 950px; overflow: hidden;
    background: var(--page);
  }
  .stage { position: relative; width: 1200px; height: 950px; }

  .card {
    position: absolute;
    width: 600px; height: 343px;
    border-radius: 4px;
    overflow: hidden;
    box-shadow: 0 6px 18px rgba(0,0,0,0.18);
  }

  /* Front */
  .card-front { left: 60px; top: 110px; background: var(--card-white); }
  .front-curve { position: absolute; inset: 0; width: 100%; height: 100%; }
  .brand-mark {
    position: absolute; left: 232px; top: 52px;
    display: flex; align-items: center; gap: 12px;
    font-family: "Roboto", sans-serif; font-weight: 500;
    color: var(--ink-dark);
  }
  .brand-dot { width: 34px; height: 34px; border-radius: 50%; background: var(--ink-dark); }
  .brand-name { font-size: 30px; line-height: 1; }
  .brand-sub { font-size: 14px; line-height: 1; margin-top: 4px; }

  .contact-block {
    position: absolute; left: 36px; top: 196px;
    font-family: "Tinos", serif; font-weight: 700;
  }
  .person-name { color: var(--accent-blue); font-size: 19px; line-height: 22px; }
  .person-title { color: var(--accent-blue); font-size: 15px; line-height: 20px; margin-bottom: 4px; }
  .contact-list { list-style: none; }
  .contact-item {
    display: flex; align-items: center; gap: 9px;
    color: var(--text-light); font-size: 14px; line-height: 21px;
  }
  .contact-icon { width: 13px; height: 13px; flex: none; }

  /* Back */
  .card-back {
    left: 540px; top: 497px; background: var(--back-blue);
    display: flex; flex-direction: column; align-items: center; justify-content: center;
    color: var(--text-light);
  }
  .back-mark { display: flex; align-items: center; gap: 16px; }
  .back-dot { width: 30px; height: 30px; border-radius: 50%; background: var(--text-light); }
  .back-name {
    font-family: "Montserrat", sans-serif; font-weight: 500;
    font-size: 40px; letter-spacing: 2px; line-height: 1;
  }
  .back-web {
    margin-top: 40px;
    font-family: "Montserrat", sans-serif; font-weight: 300;
    font-size: 12px; letter-spacing: 6px;
  }
</style>
</head>
<body>
<main class="stage">

  <section class="card card-front" aria-label="Business card front">
    <svg class="front-curve" viewBox="0 0 600 343" preserveAspectRatio="none" aria-hidden="true">
      <path d="M0,178 Q260,108 600,104 L600,343 L0,343 Z" fill="var(--accent-blue)"/>
      <path d="M0,186 Q260,116 600,112 L600,343 L0,343 Z" fill="var(--ink-dark)"/>
    </svg>

    <div class="brand-mark">
      <span class="brand-dot"></span>
      <div>
        <div class="brand-name">Career Lantern</div>
        <div class="brand-sub">Australia</div>
      </div>
    </div>

    <div class="contact-block">
      <div class="person-name">Derek Hollerby</div>
      <div class="person-title">Founder &amp; Director</div>
      <ul class="contact-list">
        <li class="contact-item">
          <svg class="contact-icon" viewBox="0 0 16 16" aria-hidden="true"><path d="M3 1h3l1.5 4-2 1.3a9 9 0 0 0 4.2 4.2L11 8.5l4 1.5v3a2 2 0 0 1-2 2A13 13 0 0 1 1 3a2 2 0 0 1 2-2z" fill="var(--accent-blue)"/></svg>
          (07) 3156 4082
        </li>
        <li class="contact-item">
          <svg class="contact-icon" viewBox="0 0 16 16" aria-hidden="true"><rect x="4" y="1" width="8" height="14" rx="1.5" fill="none" stroke="var(--accent-blue)" stroke-width="2"/></svg>
          0418 672 051
        </li>
        <li class="contact-item">
          <svg class="contact-icon" viewBox="0 0 16 16" aria-hidden="true"><rect x="1" y="3" width="14" height="10" fill="var(--accent-blue)"/><path d="M1 3l7 6 7-6" fill="none" stroke="var(--ink-dark)" stroke-width="1.5"/></svg>
          derek@careerlantern-example.com.au
        </li>
        <li class="contact-item">
          <svg class="contact-icon" viewBox="0 0 16 16" aria-hidden="true"><circle cx="8" cy="8" r="7" fill="var(--accent-blue)"/><path d="M1 8h14M8 1c-3 4-3 10 0 14M8 1c3 4 3 10 0 14" fill="none" stroke="var(--ink-dark)" stroke-width="1"/></svg>
          www.careerlantern-example.com.au
        </li>
      </ul>
    </div>
  </section>

  <section class="card card-back" aria-label="Business card back">
    <div class="back-mark">
      <span class="back-dot"></span>
      <span class="back-name">Hollerby Consulting</span>
    </div>
    <div class="back-web">www.careerlantern-example.com.au</div>
  </section>

</main>
</body>
</html>
```